Marlow Crest Group (Real Estate and Investment)

A high end, clean design.
We are a real estate company with sales, asset management and investment divisions. We want to use a black and white scheme which is really high end feel. The back of the card can just be the logo (black background with the white writing) as we will probably emboss this when we print)

Target Market(s)

High level investors, high end houses for sale

Industry/Entity Type

Business

Contact Information for Business Card

Name, position, phone number and email address
Glen Varley, Managing Director, 0437259064 and glen@marlowcrest-example.com.au

Requirements
Must have
• Back of the card to be the black background with the white writing (as per the attached images). Would like the capacity to emboss the writing and logo

```html
<!DOCTYPE html>
<html lang="en">
<head>
<meta charset="UTF-8">
<title>Marlow Crest Group — Business Card</title>
<link href="https://fonts.googleapis.com/css2?family=Lato:wght@400;700;900&display=swap" rel="stylesheet">
<style>
  :root {
    --canvas: #d9d9d9;
    --ink: #1b1b1b;
    --paper: #ffffff;
    --card-black: #1a1a1a;
    --muted: #555555;
    --rule: #333333;
  }
  * { margin: 0; padding: 0; box-sizing: border-box; }
  html, body {
    width: 1200px;
    height: 1200px;
    overflow: hidden;
    background: var(--canvas);
    font-family: "Lato", sans-serif;
  }
  .sheet {
    position: relative;
    width: 1200px;
    height: 1200px;
  }
  .card {
    position: absolute;
    left: 250px;
    width: 700px;
    height: 400px;
    box-shadow: 0 6px 18px rgba(0,0,0,0.18);
  }
  .card--back {
    top: 150px;
    background: var(--card-black);
    color: var(--paper);
    display: flex;
    align-items: center;
    justify-content: center;
  }
  .card--front {
    top: 650px;
    background: var(--paper);
    color: var(--ink);
    display: flex;
    align-items: center;
    padding-left: 70px;
  }
  .brand {
    display: flex;
    flex-direction: column;
    align-items: center;
    gap: 14px;
  }
  .brand__dot {
    width: 64px;
    height: 64px;
    border: 2px solid currentColor;
    border-radius: 50%;
  }
  .brand__name {
    font-size: 22px;
    font-weight: 400;
    letter-spacing: 0.5px;
    text-transform: uppercase;
    white-space: nowrap;
  }
  .card--front .brand { width: 230px; }
  .card--front .brand__name { font-size: 19px; }
  .details {
    display: flex;
    flex-direction: column;
    gap: 18px;
    margin-left: 26px;
  }
  .details__block {
    border-left: 2px solid var(--rule);
    padding-left: 16px;
  }
  .person__name {
    font-size: 24px;
    font-weight: 900;
    letter-spacing: 0.5px;
    text-transform: uppercase;
  }
  .person__role {
    font-size: 13px;
    color: var(--muted);
    margin-top: 2px;
  }
  .contact__line {
    display: flex;
    align-items: center;
    gap: 8px;
    font-size: 16px;
    line-height: 1.5;
  }
  .contact__icon { width: 13px; height: 13px; flex: none; }
</style>
</head>
<body>
  <main class="sheet">
    <section class="card card--back" aria-label="Card back">
      <div class="brand">
        <div class="brand__dot"></div>
        <div class="brand__name">Marlow Crest Group</div>
      </div>
    </section>

    <section class="card card--front" aria-label="Card front">
      <div class="brand">
        <div class="brand__dot"></div>
        <div class="brand__name">Marlow Crest Group</div>
      </div>
      <div class="details">
        <div class="details__block person">
          <div class="person__name">Glen Varley</div>
          <div class="person__role">Managing Director</div>
        </div>
        <div class="details__block contact">
          <div class="contact__line">
            <svg class="contact__icon" viewBox="0 0 16 16" aria-hidden="true"><path fill="#1b1b1b" d="M3 1h3l1.5 4-2 1.3a9 9 0 0 0 4.2 4.2l1.3-2L15 10v3a2 2 0 0 1-2 2A12 12 0 0 1 1 3a2 2 0 0 1 2-2z"/></svg>
            <span>0437259064</span>
          </div>
          <div class="contact__line">
            <svg class="contact__icon" viewBox="0 0 16 16" aria-hidden="true"><rect x="1" y="3" width="14" height="10" fill="#1b1b1b"/><path d="M1.5 3.5 8 9l6.5-5.5" fill="none" stroke="#fff" stroke-width="1.3"/></svg>
            <span>glen@marlowcrest-example.com.au</span>
          </div>
        </div>
      </div>
    </section>
  </main>
</body>
</html>
```